Looking for an amazing business card for a thriving DJ business

We need a business card design for a DJ company based in South Florida. The DJ company specializes in weddings, parties, bar mitzvahs, corporate events, proms, and reunions. We are looking for a modern, simple business card design. The card should state DJ Marlow K.
Updates

The name on the card should be DJ Marlow K

Industry/Entity Type

Entertainment Industry

Contact Information for Business Card

DJ Marlow K
512.447.2086
atxdjmarlowk@quellmail.com
https://www.facebook.com/DjMarlowK/
https://www.instagram.com/djmarlow.k/
www.djmarlowk.net

Font styles to use
Serif
Sans Serif

Requirements
Must have
• My business card has to be awesome.
Should not have
• The card has to have personality.

```html
<!DOCTYPE html>
<html lang="en">
<head>
<meta charset="utf-8">
<title>DJ Marlow K — Business Card</title>
<link rel="stylesheet" href="https://fonts.googleapis.com/css2?family=Cutive&family=Questrial&display=swap">
<style>
  :root {
    --page-bg: #e8e3db;
    --amber-light: #b47d38;
    --amber-mid: #8e5b22;
    --amber-dark: #5e3810;
    --disc-black: #161616;
    --disc-edge: #9a9a9a;
    --label-white: #f2f0ec;
    --label-text: #4a3a25;
    --name-ink: #ecdfc9;
    --contact-ink: #f6efe3;
    --icon-fill: #ddcfb8;
    --icon-glyph: #6b4820;
  }
  * { box-sizing: border-box; margin: 0; padding: 0; }
  html, body {
    width: 1200px; height: 969px; overflow: hidden;
    background: var(--page-bg);
  }
  .business-card {
    position: absolute; left: 155px; top: 222px;
    width: 918px; height: 523px;
    border-radius: 28px; overflow: hidden;
    background: linear-gradient(135deg, var(--amber-light) 0%, var(--amber-mid) 45%, var(--amber-dark) 100%);
    box-shadow: 0 10px 30px rgba(0,0,0,0.25);
  }
  .record-disc { position: absolute; left: 0; top: 0; }
  .brand-label {
    position: absolute; left: 232px; top: 266px;
    transform: translate(-50%, -50%);
    font-family: "Questrial", sans-serif;
    font-size: 26px; color: var(--label-text);
    letter-spacing: 0.5px;
  }
  .dj-name {
    position: absolute; right: 61px; top: 148px;
    font-family: "Cutive", serif;
    font-size: 39px; color: var(--name-ink);
    letter-spacing: 0.5px;
  }
  .contact-list {
    position: absolute; right: 62px; top: 222px;
    list-style: none;
    font-family: "Questrial", sans-serif;
    font-size: 19px; color: var(--contact-ink);
  }
  .contact-item {
    display: flex; justify-content: flex-end; align-items: center;
    gap: 10px; height: 31px;
  }
  .contact-icon { width: 22px; height: 22px; flex: none; }
  .social-row {
    position: absolute; right: 62px; top: 340px;
    display: flex; gap: 12px; align-items: center;
    font-family: "Questrial", sans-serif;
    font-size: 19px; color: var(--contact-ink);
  }
  .social-handle { display: flex; align-items: center; gap: 6px; }
  .social-mark {
    width: 18px; height: 18px; border-radius: 3px;
    background: var(--icon-fill); flex: none;
  }
</style>
</head>
<body>
  <div class="business-card">
    <svg class="record-disc" width="918" height="523" viewBox="0 0 918 523">
      <defs>
        <radialGradient id="discShade" cx="0.45" cy="0.5" r="0.6">
          <stop offset="0" stop-color="#2a2a2a"/>
          <stop offset="1" stop-color="var(--disc-black)"/>
        </radialGradient>
      </defs>
      <circle cx="145" cy="265" r="334" fill="none" stroke="var(--disc-edge)" stroke-width="3" opacity="0.8"/>
      <rect x="0" y="0" width="145" height="523" fill="url(#discShade)"/>
      <circle cx="145" cy="265" r="330" fill="url(#discShade)"/>
      <circle cx="232" cy="266" r="117" fill="var(--label-white)"/>
    </svg>
    <div class="brand-label">Groovecraft</div>

    <h1 class="dj-name">DJ Marlow K</h1>

    <ul class="contact-list">
      <li class="contact-item">
        <span>512.447.2086</span>
        <svg class="contact-icon" viewBox="0 0 22 22" aria-hidden="true">
          <circle cx="11" cy="11" r="11" fill="var(--icon-fill)"/>
          <path d="M7.5 6.5 L9.3 6.3 L10.2 8.8 L9 9.8 Q10 12 12.2 13 L13.2 11.8 L15.7 12.7 L15.5 14.5 Q11 15 7.5 10.5 Z" fill="var(--icon-glyph)"/>
        </svg>
      </li>
      <li class="contact-item">
        <span>atxdjmarlowk@quellmail.com</span>
        <svg class="contact-icon" viewBox="0 0 22 22" aria-hidden="true">
          <circle cx="11" cy="11" r="11" fill="var(--icon-fill)"/>
          <rect x="6" y="7.5" width="10" height="7" rx="1" fill="var(--icon-glyph)"/>
          <path d="M6.5 8 L11 11.5 L15.5 8" stroke="var(--icon-fill)" stroke-width="1" fill="none"/>
        </svg>
      </li>
      <li class="contact-item">
        <span>www.djmarlowk.net</span>
        <svg class="contact-icon" viewBox="0 0 22 22" aria-hidden="true">
          <circle cx="11" cy="11" r="11" fill="var(--icon-fill)"/>
          <circle cx="11" cy="11" r="5" fill="none" stroke="var(--icon-glyph)" stroke-width="1.3"/>
          <ellipse cx="11" cy="11" rx="2.2" ry="5" fill="none" stroke="var(--icon-glyph)" stroke-width="1"/>
          <line x1="6" y1="11" x2="16" y2="11" stroke="var(--icon-glyph)" stroke-width="1"/>
        </svg>
      </li>
    </ul>

    <div class="social-row">
      <span class="social-handle"><span class="social-mark"></span>DjMarlowK</span>
      <span class="social-handle"><span class="social-mark"></span>djmarlow.k</span>
    </div>
  </div>
</body>
</html>
```